TotsyPlum Business needs a Box Design

We need a box design for a new product Teething Mittens. Please check our file for a demo and Layout, Box mockup, Logo Vector
https://files.sharevault-example.com/folders/8kQzLmW3pXrT7nVb2YcHd4JfGs9Ne6Ua

Target Market(s)

A parent have baby 6 - 12 month

Industry/Entity Type

Baby

Font styles to use
Decorative
Script

Requirements
Must have
• Our logo in a Box and follow our guide
Nice to have
• Cute design

```html
<!DOCTYPE html>
<html lang="en">
<head>
<meta charset="utf-8">
<title>TotsyPlum Baby Mitten Box Dieline</title>
<link rel="stylesheet" href="https://fonts.googleapis.com/css2?family=Open+Sans:wght@300;400;600&display=swap">
<style>
  :root {
    --page: #ffffff;
    --cut-line: #4a4a4a;
    --flap-blue: #7fa9be;
    --brand-gold: #d9a35a;
    --heading-blue: #6c9cb8;
    --body-blue: #5f87a1;
    --badge-dark: #2b2420;
    --badge-gold: #b9823a;
    --mitten-tone: #eef2f5;
  }
  html, body {
    margin: 0;
    padding: 0;
    width: 1200px;
    height: 1091px;
    overflow: hidden;
    background: var(--page);
  }
  .dieline {
    display: block;
    width: 1200px;
    height: 1091px;
    font-family: "Open Sans", sans-serif;
  }
  .cut { fill: none; stroke: var(--cut-line); stroke-width: 0.8; }
  .fold { fill: none; stroke: var(--cut-line); stroke-width: 0.6; }
  .hang-slot { fill: none; stroke: var(--cut-line); stroke-width: 0.8; }
  .flap-fill { fill: var(--flap-blue); }
  .brand-name { fill: var(--brand-gold); font-size: 15px; font-weight: 400; }
  .brand-dot { fill: var(--brand-gold); }
  .section-heading { fill: var(--heading-blue); font-size: 8.6px; font-weight: 600; letter-spacing: 0.2px; }
  .section-body { fill: var(--body-blue); font-size: 8.4px; font-weight: 400; }
  .product-title { fill: #ffffff; font-size: 24px; font-weight: 400; letter-spacing: 0.5px; }
  .badge-outer { fill: var(--badge-gold); }
  .badge-inner { fill: var(--badge-dark); }
  .window { fill: #ffffff; stroke: var(--cut-line); stroke-width: 0.8; }
</style>
</head>
<body>
<svg class="dieline" viewBox="0 0 960 873" xmlns="http://www.w3.org/2000/svg">
  <defs>
    <linearGradient id="panelFade" gradientUnits="userSpaceOnUse" x1="0" y1="233" x2="0" y2="686">
      <stop offset="0" stop-color="#ffffff"/>
      <stop offset="0.22" stop-color="#ffffff"/>
      <stop offset="1" stop-color="#7ea8bd"/>
    </linearGradient>
    <linearGradient id="patternTone" gradientUnits="userSpaceOnUse" x1="352" y1="148" x2="888" y2="686">
      <stop offset="0" stop-color="#f6c9da" stop-opacity="0.55"/>
      <stop offset="0.2" stop-color="#cfe6b4" stop-opacity="0.5"/>
      <stop offset="0.4" stop-color="#c3dff5" stop-opacity="0.55"/>
      <stop offset="0.6" stop-color="#f6c9da" stop-opacity="0.5"/>
      <stop offset="0.8" stop-color="#cfe6b4" stop-opacity="0.45"/>
      <stop offset="1" stop-color="#c3dff5" stop-opacity="0.5"/>
    </linearGradient>
    <clipPath id="printArea">
      <path d="M466 233 V148 H750 V233 H864 L888 256 V668 L864 686 H352 V233 Z"/>
    </clipPath>
  </defs>

  <!-- Back panel column -->
  <g class="back-column">
    <rect class="flap-fill" x="69" y="48" width="283" height="185"/>
    <rect class="cut" x="69" y="48" width="283" height="185"/>
    <line class="fold" x1="69" y1="150" x2="352" y2="150"/>
    <path class="hang-slot" d="M196 127 h28 a5 5 0 0 1 0 10 h-8 v-2 h-12 v2 h-8 a5 5 0 0 1 0 -10 z"/>
    <path class="hang-slot" d="M196 156 h28 a5 5 0 0 1 0 10 h-8 v-2 h-12 v2 h-8 a5 5 0 0 1 0 -10 z"/>

    <rect class="cut" x="69" y="233" width="283" height="453" fill="#ffffff"/>
    <path class="cut" d="M69 686 V800 a12 12 0 0 0 12 12 H340 a12 12 0 0 0 12 -12 V686"/>
    <line class="fold" x1="69" y1="770" x2="352" y2="770"/>

    <g class="brand-lockup">
      <circle class="brand-dot" cx="209" cy="268" r="9"/>
      <text class="brand-name" x="209" y="300" text-anchor="middle">TotsyPlum</text>
    </g>

    <g class="quality-badges">
      <circle class="badge-outer" cx="130" cy="390" r="25"/>
      <circle class="badge-inner" cx="130" cy="390" r="20"/>
      <circle class="badge-outer" cx="187" cy="390" r="25"/>
      <circle class="badge-inner" cx="187" cy="390" r="20"/>
    </g>

    <path d="M232 400 C232 340 258 318 276 318 C294 318 320 340 320 400 L318 440 H234 Z" fill="var(--mitten-tone)" role="img" aria-label="Illustration of a white teething mitten with pastel handprints"/>

    <g class="product-info">
      <text class="section-heading" x="103" y="466">INSTRUCTION FOR USE</text>
      <text class="section-body" x="103" y="478">Lorem ipsum dolor sit amet, ius an clita docendi, ad</text>
      <text class="section-body" x="103" y="490">mea rebum appetere. Mea everti suscipiantur et.</text>
      <text class="section-body" x="103" y="502">Summo tollit malorum ne quo, dicta albucius vis cu,</text>
      <text class="section-body" x="103" y="514">aliquip constituto persequeris eu his.</text>

      <text class="section-heading" x="103" y="538">WASH INSTRUCTIONS</text>
      <text class="section-body" x="103" y="550">Nobis phaedrum complectitur vim ad, in est latine</text>
      <text class="section-body" x="103" y="562">gubergren, nec prima choro imperdiet eu. Maiorum</text>
      <text class="section-body" x="103" y="574">quaerendum ea qui, vidit possit voluptaria duo ei.</text>

      <text class="section-heading" x="103" y="598">WARNING</text>
      <text class="section-body" x="95" y="610">- Not suitable for children under 1 year of age</text>
      <text class="section-body" x="95" y="622">- Travel bag not meant to be used for the baby</text>
      <text class="section-body" x="95" y="634">- Do not leave bayb unsupervised with mitt</text>
      <text class="section-body" x="95" y="646">- Stop using if mitt is damaged or torn</text>
    </g>
  </g>

  <!-- Side, front and side panels -->
  <g class="print-panels">
    <rect x="466" y="105" width="284" height="128" fill="#ffffff"/>
    <g clip-path="url(#printArea)">
      <rect x="352" y="148" width="536" height="538" fill="url(#panelFade)"/>
      <rect x="352" y="148" width="536" height="538" fill="url(#patternTone)" role="img" aria-label="Scattered pastel pink, green and blue baby handprint pattern"/>
    </g>

    <path class="cut" d="M352 233 V168 H408 L466 190"/>
    <path class="cut" d="M352 686 V752 H452 L466 712 V686"/>
    <path class="cut" d="M750 190 L808 168 H864 V233"/>
    <path class="cut" d="M750 686 V712 L764 752 H864 V686"/>
    <path class="cut" d="M466 233 V118 a13 13 0 0 1 13 -13 H737 a13 13 0 0 1 13 13 V233"/>
    <line class="fold" x1="466" y1="148" x2="750" y2="148"/>
    <path class="cut" d="M864 240 L888 256 V668 L864 686"/>
    <rect class="cut" x="352" y="233" width="512" height="453"/>
    <line class="fold" x1="466" y1="233" x2="466" y2="686"/>
    <line class="fold" x1="750" y1="233" x2="750" y2="686"/>

    <g class="brand-lockup">
      <circle class="brand-dot" cx="606" cy="268" r="9"/>
      <text class="brand-name" x="606" y="300" text-anchor="middle">TotsyPlum</text>
    </g>

    <path class="window" d="M495 310 H721 V598 a13 13 0 0 1 -13 13 H508 a13 13 0 0 1 -13 -13 Z"/>

    <text class="product-title" x="607" y="657" text-anchor="middle">BABY MITTEN</text>
  </g>
</svg>
</body>
</html>
```